VELVET ORBITS - BOOK COVER

I have written a book called VELVET ORBIT - HOW TO CLIMB PAST EVERY LIMIT TO THE TOP RUNG. I need a front cover design for the book. The book cover needs to be intriguing for someone to pick it up and read the first couple of pages. I want people to think about ACHIEVING SUCCESS when they read this book.
PLEASE LOOK AT THE ATTACHMENT. THANKS!

Target Market(s)

males, entrepreneurs, small business owners, salespeople, corporate executives

Industry/Entity Type

Business

Logo Text

VELVET ORBITS

Logo styles of interest
Emblem Logo
Abstract Logo
Font styles to use
Serif
Sans Serif

Colors
ec1f27
000000
959595
ffffff

Requirements
Must have
• It has to have a "hurricane" feel to it with hurricane colors.
Nice to have
• I open to your ideas
Should not have
• no other colors except red, black, gray, white.

```html
<!DOCTYPE html>
<html lang="en">
<head>
<meta charset="utf-8">
<title>Velvet Orbit – Book Cover</title>
<link href="https://fonts.googleapis.com/css2?family=Bebas+Neue&family=Open+Sans:wght@600&display=swap" rel="stylesheet">
<style>
  :root {
    --page-bg: #efece7;
    --cover-black: #141414;
    --cover-charcoal: #262626;
    --cover-storm: #3a3a3a;
    --cover-gray: #959595;
    --ink-white: #ffffff;
    --accent-red: #ec1f27;
    --band-red-dark: #c4181f;
    --band-red-light: #d6434a;
  }
  * { margin: 0; padding: 0; box-sizing: border-box; }
  html, body {
    width: 1160px;
    height: 1200px;
    overflow: hidden;
    background: var(--page-bg);
  }
  .cover {
    position: absolute;
    left: 184px;
    top: 50px;
    width: 792px;
    height: 1100px;
    overflow: hidden;
    background: var(--cover-charcoal);
  }
  .cover__storm {
    position: absolute;
    inset: 0;
    background:
      radial-gradient(ellipse 55% 22% at 70% 30%, rgba(149,149,149,0.30), transparent 70%),
      radial-gradient(ellipse 40% 30% at 15% 55%, rgba(10,10,10,0.55), transparent 70%),
      radial-gradient(ellipse 60% 18% at 60% 68%, rgba(149,149,149,0.22), transparent 70%),
      radial-gradient(ellipse 35% 25% at 20% 85%, rgba(10,10,10,0.45), transparent 70%),
      radial-gradient(ellipse 50% 20% at 30% 8%, rgba(10,10,10,0.45), transparent 70%),
      linear-gradient(165deg, var(--cover-charcoal) 0%, var(--cover-storm) 35%, #2e2e2e 55%, var(--cover-storm) 72%, var(--cover-black) 100%);
  }
  .cover__spine-edge {
    position: absolute;
    left: 0; top: 0; bottom: 0;
    width: 12px;
    background: linear-gradient(90deg, rgba(255,255,255,0.12), rgba(0,0,0,0.3) 60%, transparent);
  }
  .title-line,
  .subtitle-line {
    position: absolute;
    left: 0; right: 0;
    text-align: center;
    font-family: 'Bebas Neue', 'Oswald', sans-serif;
    line-height: 1;
    white-space: nowrap;
  }
  .title-line {
    font-size: 144px;
    letter-spacing: 4px;
    color: var(--ink-white);
  }
  .title-line--first { top: 169px; }
  .title-line--second { top: 304px; }
  .cover__emblem {
    position: absolute;
    left: 330px;
    top: 466px;
    width: 134px;
    height: 175px;
    background: radial-gradient(ellipse 60% 55% at 50% 35%, #d6d6d6, #9a9a9a 60%, rgba(149,149,149,0) 100%);
  }
  .subtitle-line {
    font-size: 66px;
    letter-spacing: 1px;
    color: var(--accent-red);
  }
  .subtitle-line--first { top: 674px; }
  .subtitle-line--middle {
    top: 752px;
    font-size: 60px;
    color: var(--ink-white);
    display: flex;
    align-items: center;
    justify-content: center;
    gap: 24px;
  }
  .subtitle-line--last { top: 831px; }
  .subtitle__dash {
    display: inline-block;
    width: 58px;
    height: 5px;
    background: var(--ink-white);
    margin-top: -8px;
  }
  .cover__author-band {
    position: absolute;
    left: 0; right: 0;
    top: 944px;
    height: 79px;
    display: flex;
    align-items: center;
    justify-content: center;
    background: linear-gradient(90deg, var(--band-red-dark), var(--band-red-light));
  }
  .author-name {
    font-family: 'Open Sans', 'Helvetica', sans-serif;
    font-weight: 600;
    font-size: 40px;
    letter-spacing: 2px;
    color: var(--ink-white);
  }
</style>
</head>
<body>
  <main class="cover">
    <div class="cover__storm" role="img" aria-label="Dark stormy hurricane sky texture in charcoal and gray tones"></div>
    <div class="cover__spine-edge"></div>

    <h1 class="cover__title">
      <span class="title-line title-line--first">VELVET</span>
      <span class="title-line title-line--second">ORBIT</span>
    </h1>

    <div class="cover__emblem" role="img" aria-label="Small white whirlwind illustration"></div>

    <p class="cover__subtitle">
      <span class="subtitle-line subtitle-line--first">HOW TO CLIMB</span>
      <span class="subtitle-line subtitle-line--middle"><span class="subtitle__dash"></span>PAST EVERY LIMIT<span class="subtitle__dash"></span></span>
      <span class="subtitle-line subtitle-line--last">TO THE TOP RUNG</span>
    </p>

    <div class="cover__author-band">
      <span class="author-name">CALE WINTHORPE</span>
    </div>
  </main>
</body>
</html>
```